Building and Construction Business Card Design

We need a business card design for a new building and construction company called "Harbourline Estates Pty Ltd" We will build any type of building, but our main focus is luxury homes in Sydney.
We would like our business card to be elegant and strong. We have played around with colours and like greys/black and red, but are open to pretty open minded.
Updates

Project Deadline Extended
Reason: Designs are either plain without any wow, or a little comical. Hopefully we can get some designs that are more eye catching, maybe some bling (silver/ gold script) something different please. Thank you for your submissions so far.

Target Market(s)

high end real estate market

Industry/Entity Type

Construction

Contact Information for Business Card

Teodor Halloran
Director/Fully Licenced Builder
ABN: 72504918337
m: 0491 573 812
e: info@harbourlineestates.com.au
HARBOURLINE ESTATES
website: www.harbourlineestates.com.au

Building and Construction

Colors

Designer to choose colors to be used in the design.

Requirements
Nice to have
• The business name "Harbourline Estates" on one side then all the info on the otherside.

```html
<!DOCTYPE html>
<html lang="en">
<head>
<meta charset="utf-8">
<title>Harbourline Estates – Business Card</title>
<link rel="stylesheet" href="https://fonts.googleapis.com/css2?family=Tinos&family=Archivo+Black&family=Sniglet:wght@800&display=swap">
<style>
  :root {
    --card-white: #ffffff;
    --brand-red: #a61f1f;
    --ink-dark: #2b2b2b;
    --ink-black: #000000;
    --mark-blue: #2a7fbf;
    --grey-dark: #555555;
    --grey-light: #a9a9a9;
    --contact-red: #e0302c;
  }
  html, body {
    margin: 0;
    padding: 0;
    width: 1200px;
    height: 695px;
    overflow: hidden;
    background: var(--card-white);
  }
  .card {
    position: relative;
    width: 1200px;
    height: 695px;
    background: var(--card-white);
    overflow: hidden;
  }
  .card-swoosh {
    position: absolute;
    inset: 0;
    width: 1200px;
    height: 695px;
  }
  .brand {
    position: absolute;
    left: 104px;
    top: 46px;
    display: flex;
    align-items: flex-start;
    gap: 22px;
  }
  .brand-square {
    width: 100px;
    height: 100px;
    background: var(--mark-blue);
    margin-top: 4px;
  }
  .brand-text {
    display: flex;
    flex-direction: column;
  }
  .brand-name {
    font-family: "Tinos", serif;
    font-variant: small-caps;
    font-size: 50px;
    line-height: 1;
    color: var(--brand-red);
    letter-spacing: 0.5px;
  }
  .brand-tagline {
    font-family: "Archivo Black", sans-serif;
    font-size: 37px;
    line-height: 1;
    color: var(--ink-black);
    margin-top: 10px;
    margin-left: 78px;
  }
  .person {
    position: absolute;
    right: 65px;
    top: 212px;
    text-align: right;
    font-family: "Tinos", serif;
    color: var(--ink-dark);
  }
  .person-name,
  .person-role {
    font-size: 47px;
    line-height: 1.07;
  }
  .person-licence {
    font-size: 31px;
    margin-top: 20px;
    letter-spacing: -0.5px;
  }
  .contact {
    position: absolute;
    left: 28px;
    top: 538px;
    margin: 0;
    padding: 0;
    list-style: none;
    font-family: "Sniglet", sans-serif;
    font-weight: 800;
    font-size: 31px;
    line-height: 45px;
    color: var(--contact-red);
    text-shadow:
      -1.5px -1.5px 0 var(--card-white),
       1.5px -1.5px 0 var(--card-white),
      -1.5px  1.5px 0 var(--card-white),
       1.5px  1.5px 0 var(--card-white);
  }
</style>
</head>
<body>
<main class="card">
  <svg class="card-swoosh" viewBox="0 0 1200 695" aria-hidden="true">
    <defs>
      <radialGradient id="grey-panel" cx="720" cy="560" r="620" gradientUnits="userSpaceOnUse">
        <stop offset="0" stop-color="var(--grey-light)"/>
        <stop offset="1" stop-color="var(--grey-dark)"/>
      </radialGradient>
    </defs>
    <path d="M0,448 C320,405 700,440 1200,555 L1200,695 L0,695 Z" fill="url(#grey-panel)"/>
    <path d="M0,360 C260,325 620,355 1200,528 L1200,548 C640,400 280,372 0,414 Z" fill="var(--brand-red)"/>
  </svg>

  <header class="brand">
    <div class="brand-square"></div>
    <div class="brand-text">
      <span class="brand-name">Harbourline Estates Pty Ltd</span>
      <span class="brand-tagline">Building &amp; Construction</span>
    </div>
  </header>

  <section class="person">
    <div class="person-name">Teodor Halloran</div>
    <div class="person-role">Director</div>
    <div class="person-licence">Fully Licenced Builder ABN: 72504918337</div>
  </section>

  <ul class="contact">
    <li>mob: 0491 573 812</li>
    <li>email: info@harbourlineestates.com.au</li>
    <li>website: www.harbourlineestates.com.au</li>
  </ul>
</main>
</body>
</html>
```